Birchwell Craft House business card design- Fine Art sculpture business (Contract guaranteed)

This business card is for a fine art business. Though we don't have a website up and running yet it should be up soon. I would like the business card to be elegant and fairly simple with a picture of one of my sculptures on the front (you might need to photoshop out the background) as well as my basic contact info (my name,phone # and e-mail). On the back I'd like it to be pretty simple with just "Notes" and some blank lines for writing in info.
Updates

Target Market(s)

High end artwork buyers

Industry/Entity Type

Art Gallery

Contact Information for Business Card

Wendell Marsh Phone: (555) 312-4098 E-mail: wendell@quarrymint.example Facebook: @birchwellcrafthouse Instagram: birchwellcrafthouse

Colors

Designer to choose colors to be used in the design.

Requirements
Must have
• *A picture of one of my sculptures*, my name, business name (Birchwell Craft House), e-mail, phone #, and a notes section on the back.
• Birchwell Craft House
• Wendell Marsh
• (555)312-4098
• wendell@quarrymint.example
• Facebook: @birchwellcrafthouse
• Instagram: birchwellcrafthouse
Nice to have
• It'd be nice if you can crop out the background in the sculpture pictures, which ever one you end up using.

```html
<!DOCTYPE html>
<html lang="en">
<head>
<meta charset="utf-8">
<title>Birchwell Craft House – Business Card</title>
<link href="https://fonts.googleapis.com/css2?family=Pinyon+Script&family=Roboto:wght@400;500&display=swap" rel="stylesheet">
<style>
  :root {
    --stage: #6b5343;
    --card-dark: #1e1f22;
    --card-dark-edge: #2a2b2f;
    --card-light: #f1f1f1;
    --card-light-shade: #e1e1e3;
    --violet-soft: #ad6ae6;
    --violet-strong: #8b3fd8;
    --ink-light: #ececec;
    --rule: #6e6e6e;
    --shadow: rgba(0, 0, 0, 0.45);
  }
  * { margin: 0; padding: 0; box-sizing: border-box; }
  html, body {
    width: 1200px;
    height: 960px;
    overflow: hidden;
    background: var(--stage);
  }
  .canvas {
    position: relative;
    width: 1200px;
    height: 960px;
  }
  .card {
    position: absolute;
    width: 600px;
    height: 343px;
    box-shadow: 0 3px 6px var(--shadow);
  }
  .card-front {
    left: 302px;
    top: 124px;
    background: radial-gradient(ellipse at 60% 40%, var(--card-dark-edge) 0%, var(--card-dark) 70%);
  }
  .sculpture-photo {
    position: absolute;
    left: 388px;
    top: 172px;
    width: 100px;
    height: 248px;
  }
  .card-front .sculpture-photo { left: 86px; top: 48px; }
  .studio-name {
    position: absolute;
    left: 250px;
    top: 92px;
    font-family: "Pinyon Script", cursive;
    font-size: 34px;
    line-height: 1;
    color: var(--violet-soft);
    white-space: nowrap;
  }
  .owner-name {
    position: absolute;
    left: 251px;
    top: 153px;
    font-family: "Roboto", sans-serif;
    font-weight: 500;
    font-size: 21px;
    line-height: 1;
    color: var(--violet-strong);
    text-transform: uppercase;
    letter-spacing: 0.2px;
  }
  .contact-list {
    position: absolute;
    left: 252px;
    top: 194px;
    list-style: none;
    font-family: "Roboto", sans-serif;
    font-size: 14.5px;
    color: var(--ink-light);
  }
  .contact-item {
    display: flex;
    align-items: center;
    height: 19.5px;
  }
  .contact-icon {
    width: 12px;
    height: 12px;
    margin-right: 9px;
    fill: var(--violet-soft);
  }
  .card-back {
    left: 299px;
    top: 493px;
    background: linear-gradient(160deg, var(--card-light) 0%, var(--card-light-shade) 55%, var(--card-light) 100%);
  }
  .note-line {
    position: absolute;
    left: 46px;
    width: 508px;
    height: 0;
    border-top: 1.5px solid var(--rule);
  }
</style>
</head>
<body>
<main class="canvas">
  <section class="card card-front">
    <svg class="sculpture-photo" viewBox="0 0 100 248" role="img" aria-label="Photograph of an amethyst crystal sculpture on a stone base">
      <defs>
        <linearGradient id="amethyst" x1="0" y1="0" x2="0" y2="1">
          <stop offset="0" stop-color="#6a3bb0"/>
          <stop offset="0.5" stop-color="#4b2a8a"/>
          <stop offset="0.85" stop-color="#5a35a0"/>
          <stop offset="1" stop-color="#8a8a86"/>
        </linearGradient>
      </defs>
      <rect width="100" height="248" rx="18" fill="url(#amethyst)"/>
    </svg>

    <h1 class="studio-name">Birchwell Craft House</h1>
    <p class="owner-name">Wendell Marsh</p>
    <ul class="contact-list">
      <li class="contact-item">
        <svg class="contact-icon" viewBox="0 0 24 24" aria-hidden="true"><path d="M6.6 10.8a15.1 15.1 0 0 0 6.6 6.6l2.2-2.2a1 1 0 0 1 1-.25 11.4 11.4 0 0 0 3.6.57 1 1 0 0 1 1 1V20a1 1 0 0 1-1 1A17 17 0 0 1 3 4a1 1 0 0 1 1-1h3.5a1 1 0 0 1 1 1c0 1.25.2 2.45.57 3.57a1 1 0 0 1-.25 1z"/></svg>
        <span>(555) 312-4098</span>
      </li>
      <li class="contact-item">
        <svg class="contact-icon" viewBox="0 0 24 24" aria-hidden="true"><path d="M2 5h20v14H2z M2 5l10 7 10-7" /><path d="M3 6.5l9 6.3 9-6.3V18H3z" fill="#1e1f22"/><path d="M2 5h20l-10 7z"/></svg>
        <span>wendell.marsh4@quarrymint.example</span>
      </li>
      <li class="contact-item">
        <svg class="contact-icon" viewBox="0 0 24 24" aria-hidden="true"><circle cx="12" cy="12" r="10"/><path d="M8 6c2 1 3 3 2 5s-3 2-3 4M14 4c-1 2 1 3 3 3M15 14c2 0 3 2 2 4" stroke="#1e1f22" stroke-width="1.6" fill="none"/></svg>
        <span>www.birchwellcrafthouse.com</span>
      </li>
    </ul>
  </section>

  <section class="card card-back" aria-label="Notes side">
    <div class="note-line" style="top:68px"></div>
    <div class="note-line" style="top:123px"></div>
    <div class="note-line" style="top:177px"></div>
    <div class="note-line" style="top:232px"></div>
    <div class="note-line" style="top:286px"></div>
  </section>
</main>
</body>
</html>
```